Our business deals with residential and commercial property management. We have commercial tenants willing to offer deals to our residential tenants. We want a very nice looking card stock where I can add (later) each specific deal/incentive. The template attached has two options but feel free to come up with what you think looks best. We need or logo and possibly this simple phrase as the title,

"Welcome to the Brelford Community!" OR "Join the Brelford Community"

This is optional, use discretion on what is should say:

"Every member of Brelford Commercial is important to us, be a part of our community and explore your neighborhood."

www.brelfordcommercial.example can give you a feel for our look and image. I was thinking of maybe a red & black color scheme.

***Each slot for the deal should be blank so I can add and change each deal later. These are going to be cut out so maybe the "-----" lines around the deals would look good. Thanks!!

Target Market(s)

Residential Tenants: Single & Multi Families

Industry/Entity Type

Property Management

Font styles to use
Serif

Colors
ec1f27
000000
fbfbfb

Requirements
Must have
• -Logo (Attached)
• -6 blank slots to add deals later (Can have more deals based on appropriate look)
• -either "Welcome to the Brelford Community" or "Join the Brelford Community"
• -Our phone number: 801.555.0147
• -Website: www.brelfordcommercial.example
• -Address: 417 E. Dunmore Way Suite 5, Centerville, UT 84099
Nice to have
• "Every member of Brelford Commercial is important to us, be a part of our community and explore your neighborhood."
• This could be something else that's similar but sounds better.
• Possible color options: red, black, white OR Your discretion.
Should not have
• Pictures of properties or people.

```html
<!DOCTYPE html>
<html lang="en">
<head>
<meta charset="utf-8">
<title>Brelford Community Deals Card</title>
<link rel="stylesheet" href="https://fonts.googleapis.com/css2?family=Noto+Serif:wght@400;700&display=swap">
<style>
  :root {
    --brand-red: #ec1f27;
    --deep-red: #c3141b;
    --ink: #000000;
    --paper: #fbfbfb;
    --text-grey: #333333;
    --panel-light: #f1eeee;
    --panel-mid: #e2dcdc;
    --panel-dark: #cfc7c7;
    --cut-line: #8a8a8a;
  }
  * { box-sizing: border-box; margin: 0; padding: 0; }
  html, body { width: 878px; height: 1200px; overflow: hidden; background: var(--paper); }
  .card {
    position: relative;
    width: 878px;
    height: 1200px;
    background: radial-gradient(ellipse at center, #ffffff 55%, #ececec 100%);
    font-family: "Noto Serif", Georgia, serif;
    color: var(--ink);
  }
  .card-title {
    position: absolute;
    top: 38px; left: 0; width: 100%;
    text-align: center;
    font-size: 42px;
    font-weight: 400;
    color: var(--brand-red);
  }
  .feature-grid {
    position: absolute;
    top: 112px; left: 34px;
    width: 804px; height: 508px;
    border: 3px solid var(--brand-red);
  }
  .feature-tile {
    position: absolute;
    border: 2px solid var(--brand-red);
  }
  .tile-top-left { left: 2px; top: 2px; width: 251px; height: 144px;
    background: linear-gradient(135deg, var(--panel-light), var(--panel-mid)); }
  .tile-top-mid { left: 259px; top: 2px; width: 251px; height: 144px;
    background: linear-gradient(135deg, var(--panel-mid), var(--panel-light)); }
  .tile-large { left: 2px; top: 152px; width: 508px; height: 348px;
    background: linear-gradient(160deg, var(--panel-light) 10%, var(--panel-mid) 60%, var(--panel-dark)); }
  .tile-tall { left: 516px; top: 2px; width: 280px; height: 498px;
    background: linear-gradient(180deg, var(--panel-dark) 0%, var(--panel-light) 50%, var(--panel-mid) 100%); }
  .brand-name {
    position: absolute;
    top: 648px; left: 62px;
    display: flex; align-items: center; gap: 12px;
    font-size: 30px; font-weight: 700;
    color: var(--ink);
    line-height: 1.05;
  }
  .brand-mark { width: 22px; height: 22px; background: var(--brand-red); flex: none; }
  .contact {
    position: absolute;
    top: 628px; left: 420px;
    list-style: none;
    font-size: 21px;
    color: var(--brand-red);
  }
  .contact li { display: flex; align-items: flex-start; gap: 10px; margin-bottom: 12px; }
  .contact svg { flex: none; width: 20px; height: 20px; margin-top: 4px; }
  .contact .address { color: var(--ink); }
  .deals {
    position: absolute;
    top: 774px; left: 125px;
    display: grid;
    grid-template-columns: repeat(3, 184px);
    column-gap: 33px; row-gap: 12px;
  }
  .deal-cut {
    padding: 5px;
    border: 2px dashed var(--cut-line);
  }
  .deal-slot {
    height: 94px;
    display: flex; align-items: center; justify-content: center;
    background: linear-gradient(180deg, var(--brand-red), var(--deep-red));
    color: #ffffff;
    font-size: 22px;
    box-shadow: 0 2px 4px rgba(0,0,0,0.25);
  }
  .closing-note {
    position: absolute;
    top: 1024px; left: 60px; width: 758px;
    text-align: center;
    font-size: 27px; line-height: 1.3;
    color: var(--text-grey);
  }
</style>
</head>
<body>
<main class="card">
  <h1 class="card-title">Welcome to the Brelford Community</h1>

  <section class="feature-grid">
    <div class="feature-tile tile-top-left" role="img" aria-label="Soft neutral colour panel"></div>
    <div class="feature-tile tile-top-mid" role="img" aria-label="Soft neutral colour panel"></div>
    <div class="feature-tile tile-large" role="img" aria-label="Soft neutral colour panel"></div>
    <div class="feature-tile tile-tall" role="img" aria-label="Soft neutral colour panel"></div>
  </section>

  <div class="brand-name"><span class="brand-mark"></span><span>Brelford<br>Commercial</span></div>

  <ul class="contact">
    <li>
      <svg viewBox="0 0 20 20"><circle cx="10" cy="10" r="8.5" fill="none" stroke="#000" stroke-width="1.5"/><path d="M7 5.5l2 2-1 1.2c.6 1.3 1.5 2.2 2.8 2.8l1.2-1 2 2-1.3 1.5C9.5 13.7 6.3 10.5 5.5 7.3z" fill="#000"/></svg>
      <span>801.555.0147</span>
    </li>
    <li>
      <svg viewBox="0 0 20 20"><circle cx="10" cy="10" r="8.5" fill="none" stroke="#000" stroke-width="1.5"/><ellipse cx="10" cy="10" rx="3.5" ry="8.5" fill="none" stroke="#000" stroke-width="1.2"/><line x1="1.5" y1="10" x2="18.5" y2="10" stroke="#000" stroke-width="1.2"/></svg>
      <span>www.brelfordcommercial.example</span>
    </li>
    <li class="address">
      <svg viewBox="0 0 20 20"><path d="M10 2L1.5 10H4v8h4.5v-5h3v5H16v-8h2.5z" fill="#000"/></svg>
      <span>417 E. Dunmore Way Suite 5<br>Centerville, UT 84099</span>
    </li>
  </ul>

  <section class="deals">
    <div class="deal-cut"><div class="deal-slot">Add Deals</div></div>
    <div class="deal-cut"><div class="deal-slot">Add Deals</div></div>
    <div class="deal-cut"><div class="deal-slot">Add Deals</div></div>
    <div class="deal-cut"><div class="deal-slot">Add Deals</div></div>
    <div class="deal-cut"><div class="deal-slot">Add Deals</div></div>
    <div class="deal-cut"><div class="deal-slot">Add Deals</div></div>
  </section>

  <p class="closing-note">Every member of Brelford Commercial is important to us be a part of our community and explore your neighborhood.</p>
</main>
</body>
</html>
```